Book cover for a book about time management for women

We need a book cover for a book about time management for women written by a woman. Even though the book has a provocative title "Calendar candy" based on the seminars the author holds for women seeking the change in their life, it has nothing to do with the words themselves. The subtitle is "Keep each morning in your grip. A bold guide on daily rhythm for ladies today"

Preferred fonts (not necessarily):
Plus Jakarta Sans
Tiempos Headline

Preferred colours (not necessarily):
- orange
- pastel "highlighters"

We look for a simple/clean design that catches the attention of the women without too many graphic elements.

Target Market(s)

Women that want to change and organise their life

Industry/Entity Type

productivity, marketing, work-life balance

Font styles to use
Other font styles liked:
• Plus Jakarta Sans, Tiempos Headline

Colors
F0912C
F2A743
F7CA91
FBE8D2
FDF5EE
A7469A
B969AE
D3A5CF
EDDBEB
F8F0F9

Requirements
Must have
• Famine feeling as the target audience are women with drive to better life
Should not have
• No explicit images or sexually motivated themes

```html
<!DOCTYPE html>
<html lang="en">
<head>
<meta charset="utf-8">
<title>Calendar Candy — Book Cover</title>
<link rel="stylesheet" href="https://fonts.googleapis.com/css2?family=Playfair+Display:wght@600&family=Plus+Jakarta+Sans:wght@500;800&display=swap">
<style>
  :root {
    --page-bg: #e6e6e6;
    --cover-white: #ffffff;
    --cover-shade: #e4e4e4;
    --title-orange: #f0912c;
    --title-plum: #a7469a;
    --rule-tan: #dcc4a6;
    --ink: #1d1d1f;
    --skin-light: #f1d6c6;
    --skin-mid: #d9a98f;
  }
  * { margin: 0; padding: 0; box-sizing: border-box; }
  html, body {
    width: 1200px;
    height: 800px;
    overflow: hidden;
    background: var(--page-bg);
  }
  .stage {
    width: 1200px;
    height: 800px;
    display: flex;
    align-items: center;
    justify-content: center;
  }
  .book-cover {
    position: relative;
    width: 480px;
    height: 720px;
    background: radial-gradient(ellipse 60% 55% at 50% 50%, var(--cover-shade) 0%, var(--cover-white) 100%);
    overflow: hidden;
  }
  .title {
    position: absolute;
    left: 0;
    right: 0;
    top: 132px;
    text-align: center;
    white-space: nowrap;
  }
  .title-top {
    display: block;
    font-family: "Playfair Display", Georgia, serif;
    font-weight: 600;
    font-size: 62px;
    line-height: 1;
    letter-spacing: 4px;
    color: var(--title-orange);
    text-transform: uppercase;
  }
  .title-bottom {
    display: block;
    margin-top: 6px;
    font-family: "Plus Jakarta Sans", Helvetica, sans-serif;
    font-weight: 800;
    font-size: 96px;
    line-height: 1;
    letter-spacing: -2px;
    color: var(--title-plum);
    text-transform: uppercase;
  }
  .divider {
    position: absolute;
    top: 373px;
    left: 50%;
    width: 87px;
    height: 1px;
    margin-left: -43px;
    background: var(--rule-tan);
  }
  .subtitle {
    position: absolute;
    left: 0;
    right: 0;
    top: 387px;
    text-align: center;
    font-family: "Plus Jakarta Sans", Helvetica, sans-serif;
    font-weight: 500;
    color: var(--ink);
    text-transform: uppercase;
  }
  .subtitle-lead {
    display: block;
    font-size: 12px;
    letter-spacing: 1.2px;
  }
  .subtitle-line {
    display: block;
    margin-top: 6px;
    font-size: 8.5px;
    letter-spacing: 0.6px;
  }
  .cover-photo {
    position: absolute;
    left: 74px;
    width: 336px;
    bottom: 0;
    height: 140px;
    background: linear-gradient(to top, var(--skin-mid) 0%, var(--skin-light) 55%, rgba(241, 214, 198, 0) 100%);
  }
</style>
</head>
<body>
  <main class="stage">
    <section class="book-cover">
      <h1 class="title">
        <span class="title-top">Calendar</span>
        <span class="title-bottom">Candy</span>
      </h1>
      <div class="divider"></div>
      <p class="subtitle">
        <span class="subtitle-lead">Keep each morning in your grip.</span>
        <span class="subtitle-line">A bold guide on daily rhythm for ladies today</span>
      </p>
      <div class="cover-photo" role="img" aria-label="Photo of a row of women's raised arms with clenched fists rising from the bottom edge"></div>
    </section>
  </main>
</body>
</html>
```